Recipe Card Design

I have a small kitchen store in Livingston Montana, and I would like to have recipe cards (4x6 postcard) designed with my logo, lines for recipe writing, all in black and white. My website is here: www.copperladlehouse.com

Store

```html
<!DOCTYPE html>
<html lang="en">
<head>
<meta charset="utf-8">
<title>Copper Ladle House – Recipe Card</title>
<link rel="stylesheet" href="https://fonts.googleapis.com/css2?family=Courier+Prime:wght@400;700&family=Dancing+Script:wght@600&display=swap">
<style>
  :root {
    --ink: #1c1818;
    --paper: #ffffff;
    --backdrop: #ece9e4;
    --rule: #3a3535;
  }
  * { margin: 0; padding: 0; box-sizing: border-box; }
  html, body {
    width: 1200px;
    height: 1000px;
    overflow: hidden;
    background: var(--backdrop);
  }
  .sheet {
    position: relative;
    width: 1200px;
    height: 1000px;
  }
  .card {
    position: absolute;
    left: 311px;
    width: 580px;
    height: 448px;
    background: var(--paper);
    box-shadow: 0 1px 3px rgba(0,0,0,0.18);
  }
  .card--front { top: 45px; }
  .card--back { top: 515px; }
  .card__frame {
    position: absolute;
    inset: 0;
    width: 580px;
    height: 448px;
  }
  .brand {
    position: absolute;
    left: 0;
    right: 0;
    top: 176px;
    text-align: center;
    font-family: "Courier Prime", monospace;
    font-weight: 700;
    font-size: 42px;
    line-height: 1.1;
    color: var(--ink);
    letter-spacing: 1px;
  }
  .recipe-banner {
    position: absolute;
    left: 66px;
    top: 57px;
    width: 229px;
    height: 58px;
  }
  .recipe-banner__title {
    position: absolute;
    left: 97px;
    top: 56px;
    width: 165px;
    height: 46px;
    display: flex;
    align-items: center;
    justify-content: center;
    font-family: "Dancing Script", cursive;
    font-weight: 600;
    font-size: 27px;
    color: var(--paper);
  }
  .postage {
    position: absolute;
    left: 432px;
    top: 42px;
    width: 101px;
    height: 101px;
  }
  .postage__label {
    position: absolute;
    left: 432px;
    top: 42px;
    width: 101px;
    height: 101px;
    display: flex;
    flex-direction: column;
    align-items: center;
    justify-content: center;
    gap: 8px;
    font-family: "Courier Prime", monospace;
    font-size: 10px;
    letter-spacing: 1.5px;
    color: var(--paper);
  }
  .address-lines {
    position: absolute;
    left: 325px;
    top: 196px;
    width: 203px;
  }
  .address-lines__line {
    height: 37px;
    border-bottom: 1.5px solid var(--rule);
  }
  .address-lines__line:first-child { height: 1px; }
  .web {
    position: absolute;
    left: 0;
    right: 0;
    top: 388px;
    text-align: center;
    font-family: "Courier Prime", monospace;
    font-size: 12px;
    letter-spacing: 0.8px;
    color: var(--ink);
  }
</style>
</head>
<body>
<main class="sheet">

  <section class="card card--front" aria-label="Recipe card front">
    <svg class="card__frame" viewBox="0 0 580 448" aria-hidden="true">
      <path d="M36 20 H544 A14 14 0 0 0 558 34 V414 A14 14 0 0 0 544 428 H36 A14 14 0 0 0 22 414 V34 A14 14 0 0 0 36 20 Z"
            fill="none" stroke="var(--ink)" stroke-width="5"/>
      <path d="M40 29 H540 A10 10 0 0 0 550 39 V409 A10 10 0 0 0 540 419 H40 A10 10 0 0 0 30 409 V39 A10 10 0 0 0 40 29 Z"
            fill="none" stroke="var(--ink)" stroke-width="1.2"/>
    </svg>
    <p class="brand">Copper Ladle<br>House</p>
  </section>

  <section class="card card--back" aria-label="Recipe card back">
    <svg class="card__frame" viewBox="0 0 580 448" aria-hidden="true">
      <path d="M36 20 H544 A14 14 0 0 0 558 34 V414 A14 14 0 0 0 544 428 H36 A14 14 0 0 0 22 414 V34 A14 14 0 0 0 36 20 Z"
            fill="none" stroke="var(--ink)" stroke-width="5"/>
      <path d="M40 29 H540 A10 10 0 0 0 550 39 V409 A10 10 0 0 0 540 419 H40 A10 10 0 0 0 30 409 V39 A10 10 0 0 0 40 29 Z"
            fill="none" stroke="var(--ink)" stroke-width="1.2"/>
    </svg>

    <svg class="recipe-banner" viewBox="0 0 229 58" aria-hidden="true">
      <polygon points="0,16 50,16 50,56 0,56 14,36" fill="var(--ink)"/>
      <polygon points="229,16 179,16 179,56 229,56 215,36" fill="var(--ink)"/>
      <rect x="31" y="0" width="165" height="44" fill="var(--ink)"/>
      <rect x="35" y="4" width="157" height="36" fill="none" stroke="var(--paper)" stroke-width="1"/>
    </svg>
    <span class="recipe-banner__title">My Recipes</span>

    <svg class="postage" viewBox="0 0 101 101" aria-hidden="true">
      <rect x="0" y="0" width="101" height="101" fill="var(--ink)"/>
      <rect x="9" y="9" width="83" height="83" fill="none" stroke="var(--paper)" stroke-width="1.5"/>
    </svg>
    <div class="postage__label"><span>POSTAGE</span><span>AREA</span></div>

    <div class="address-lines" aria-hidden="true">
      <div class="address-lines__line"></div>
      <div class="address-lines__line"></div>
      <div class="address-lines__line"></div>
      <div class="address-lines__line"></div>
      <div class="address-lines__line"></div>
    </div>

    <p class="web">www.copperladlehouse.com</p>
  </section>

</main>
</body>
</html>
```